Business school needs a web design

Who We are:
KRVT is a small business school that offers programs in Project Management. The school is based in West Africa and welcomes students from the whole area. Our aim is to become one of the reference business schools in Africa.

Project Brief:
The site will include all informations relevant for different types of visitors that we have: actual and future students, companies, mass media, future employees, ect. It will present information about subscription, list of programs, presentation of the school and its team,etc.

What We want:
This competition is for Design only no coding! We need design for two pages.
We did some wireframing for the home page and the list of programs page. We made them just to show how we imagine the website would look like. But we encourage creative designs, so you don't have to stick to the wireframe models.

Sites We like:
http://www.ravenmoorcollege.example/
http://www.belvantis.example/fr/etudes.html
http://www.qtl.example/mba/Pages/default.aspx

Color schemes
The logo of the school is red and black. So the color scheme of the website should match that. For the rest, it is opened to your imagination.
Updates

The payment for the project is now garanteed. Good luck to you all !

Target Market(s)

The target market is diversified because we have students of different ages, also company representatives or employees that might visit the website for recruitment purposes. But the majority of our audience should be aged between 20 - 30 years.

Industry/Entity Type

Small Business

Requirements
Must have
• The design must include two pages: a home page and another interior page : might be the list of programs or any other page relevant to the domain. The Home page must include a slide show at the beginning.
The background page must be white.
Nice to have
• The use of flat design for this project is preferred.
The use of Pelican scaffold as a base for the design is an asset.

```html
<!DOCTYPE html>
<html lang="fr">
<head>
<meta charset="utf-8">
<title>KRVT – Ecole de Management de Projet</title>
<link rel="stylesheet" href="https://fonts.googleapis.com/css2?family=Open+Sans:wght@400;600;700&display=swap">
<style>
:root{
  --red:#b30008;
  --red-dark:#8f0006;
  --red-head:#c8000b;
  --ink:#222;
  --text:#3a3a3a;
  --grey-panel:#efefef;
  --grey-card:#dedede;
  --line:#d6d6d6;
  --dark:#2b2724;
  --dark-2:#1f1c1a;
  --white:#fff;
}
*{margin:0;padding:0;box-sizing:border-box}
html,body{width:758px;height:1200px;overflow:hidden;background:var(--white)}
body{position:relative;font-family:"Open Sans",Arial,sans-serif;color:var(--text)}
a{color:inherit;text-decoration:none}
.abs{position:absolute}

/* header */
.site-header{left:0;top:0;width:758px;height:74px;background:linear-gradient(90deg,#a80008,#c6000a 30%,#c30009 70%,#a50007)}
.brand{left:100px;top:10px;width:58px;height:50px;display:flex;align-items:center;justify-content:center;gap:4px;color:var(--white);font-weight:700;font-size:13px}
.brand .dot{width:8px;height:8px;border-radius:50%;background:var(--white)}
.social{left:294px;top:21px;display:flex;gap:5px}
.social span{width:6px;height:6px;border-radius:50%;background:var(--white)}
.util-nav{left:350px;top:20px;font-size:5.6px;color:var(--white);white-space:nowrap}
.util-nav span{margin:0 3px}
.search{left:588px;top:20px;width:70px;height:11px;background:var(--white);border-radius:6px;font-size:5.5px;color:#999;padding:1.5px 0 0 6px}
.search svg{position:absolute;right:5px;top:2.5px}
.main-nav{left:198px;top:42px;display:flex;gap:7px;font-size:7.3px;font-weight:600;color:var(--white);white-space:nowrap}
.main-nav .sep{opacity:.8}
.main-nav .active{border-top:1px solid rgba(255,255,255,.7);border-bottom:1px solid rgba(255,255,255,.7);padding:0 0 1px;margin-top:-3px;padding-top:3px}

/* slider */
.slider{left:99px;top:74px;width:560px;height:309px;background:linear-gradient(100deg,#e8e4df 0%,#d9dde3 30%,#c7d1dd 55%,#b8c2cf 80%,#dfe4ea 100%)}
.slide-arrow{top:122px}
.caption{left:0;bottom:0;width:560px;height:35px;background:rgba(35,35,40,.82);color:var(--white);font-size:8.8px;padding:10px 0 0 14px}
.dots{right:14px;top:13px;display:flex;gap:2px}
.dots span{width:6px;height:6px;border-radius:50%;border:1px solid #ccc}
.dots .on{background:var(--white);border:2px solid var(--red)}

/* intro */
.intro{left:124px;top:414px;width:512px;text-align:center}
.intro h1{font-size:14.5px;font-weight:700;color:var(--red);margin-bottom:5px}
.intro p{font-size:7.2px;line-height:9.6px;color:#444}
.intro .more{display:inline-block;margin-top:6px;font-size:6.5px;color:var(--red);text-decoration:underline}

/* content panel */
.panel{left:99px;top:512px;width:427px;height:406px;background:linear-gradient(180deg,#f2f2f2,#fbfbfb 60%,#f0f0f0);border:1px solid #e4e4e4}
.section-title{font-size:13.5px;font-weight:700;color:var(--ink);display:flex;align-items:center;gap:6px}
.section-title::after{content:"";flex:1;height:1px;background:var(--line);margin-top:6px}
.blog-title{left:15px;top:17px;width:393px}
.blog-item{width:190px;height:56px}
.thumb{width:58px;height:56px;background:linear-gradient(135deg,#8b7d6d,#4d4540 55%,#cfc7bd)}
.date-tag{left:0;bottom:0;width:32px;height:9px;background:var(--red);color:var(--white);font-size:5.5px;padding:1px 0 0 5px}
.blog-text{left:63px;top:3px;width:126px;font-size:6.3px;line-height:7.8px;color:#333}
.blog-text b{display:block;color:var(--ink)}
.meta{color:var(--red);margin-top:1px}
.meta u{margin-left:3px}
.v-div{left:210px;top:46px;width:1px;height:168px;background:var(--line)}
.h-div{left:15px;top:121px;width:393px;height:1px;background:var(--line)}

.events-title{left:15px;top:217px;width:254px}
.event-card{width:123px;height:126px;background:var(--grey-card);top:244px}
.ribbon{left:0;top:0}
.ribbon span{position:absolute;left:0;top:2px;width:20px;text-align:center;color:var(--white);font-size:8px;line-height:7px}
.ribbon span small{font-size:5px}
.event-text{left:25px;top:14px;width:92px;font-size:6.4px;line-height:8px;color:#333}
.event-text b{display:block;color:var(--ink)}
.event-more{right:10px;bottom:10px;font-size:6.4px;color:var(--red);text-decoration:underline}

.tv-title{left:285px;top:217px;width:122px}
.video{left:287px;top:245px;width:119px;height:125px;background:linear-gradient(160deg,#d9dfe3,#b7b2ac 45%,#9aa4ae)}
.play{left:47px;top:48px;width:24px;height:24px;border-radius:50%;border:2px solid #111;background:rgba(255,255,255,.25)}
.controls{left:0;bottom:0;width:119px;height:18px;background:#111;color:#ddd;font-size:5px}
.video-label{left:287px;top:374px;font-size:6.4px;color:#333}

/* sidebar */
.side-box{left:540px;width:119px}
.news{top:512px;height:190px;background:var(--red-head)}
.side-tab{left:0;top:0;height:17px;background:var(--dark-2);color:var(--white);font-size:9px;font-weight:600;padding:2px 0 0 10px}
.news .side-tab{width:86px;clip-path:polygon(0 0,100% 0,92% 100%,0 100%)}
.news-item{left:10px;width:104px;height:30px}
.news-thumb{left:0;top:0;width:34px;height:27px;background:linear-gradient(135deg,#9c8e7f,#4f4843 60%,#c9c1b6);border:1px solid rgba(255,255,255,.6)}
.news-text{left:40px;top:0;width:64px;font-size:6.3px;line-height:7.4px;color:#fbe4e4}
.news-text b{display:block;color:var(--white)}
.view-all{right:12px;top:168px;font-size:6.3px;color:var(--white);text-decoration:underline}

.audience{top:718px;height:196px;background:linear-gradient(120deg,#2c2a2a 40%,#4a4440 75%,#5d554f)}
.audience .side-tab{width:86px;background:var(--red-head);clip-path:polygon(0 0,100% 0,92% 100%,0 100%)}
.audience ul{position:absolute;left:11px;top:22px;list-style:none}
.audience li{font-size:6.6px;color:#eee;height:16px;width:64px;border-bottom:1px solid rgba(255,255,255,.12);display:flex;align-items:center;gap:4px}
.audience li::before{content:"";width:4px;height:4px;background:#bbb}
.more-links{right:10px;bottom:8px;font-size:6.3px;color:var(--white);text-decoration:underline}

/* partners */
.partners{left:0;top:952px;width:758px;height:50px;border-top:1px solid #e3e3e3;display:flex;justify-content:center;align-items:center;gap:26px}
.partners span{width:56px;height:16px;border-radius:3px;background:#c9c9c9}

/* footer */
.site-footer{left:0;top:1002px;width:758px;height:163px;background:var(--dark)}
.foot-col{top:33px;color:#ddd}
.foot-col h3{font-size:10.5px;font-weight:600;color:var(--white);display:flex;align-items:center;gap:5px;margin-bottom:6px}
.foot-col h3 svg{flex:none}
.foot-col ul{list-style:none}
.foot-col li{font-size:6.3px;height:14.2px;display:flex;align-items:center;gap:4px}
.foot-col li::before{content:"";width:5px;height:5px;border-radius:50%;background:#ddd}
.foot-col p{font-size:6.3px;line-height:9px}
.phone{display:flex;gap:6px;margin-top:4px;font-size:6.3px;line-height:9.2px}
.foot-social{display:flex;gap:10px;margin-top:8px}
.foot-social span{width:6px;height:6px;border-radius:50%;background:#ddd}
.email{width:120px;height:18px;background:#f4f4f4;border:1px solid #999;font-size:6.2px;color:#777;padding:4px 0 0 8px;margin-top:7px}
.subscribe{display:inline-block;margin-top:5px;background:#1c1a18;color:var(--white);font-size:9px;font-weight:600;padding:2px 10px 3px}
.foot-brand{left:592px;top:12px;width:76px;height:76px;border-radius:50%;background:radial-gradient(circle,#5a5550,rgba(43,39,36,0) 70%);display:flex;align-items:center;justify-content:center;gap:4px;color:#8a8580;font-weight:700;font-size:11px}
.foot-brand .dot{width:7px;height:7px;border-radius:50%;background:#8a8580}
.copyright{left:0;top:1165px;width:758px;height:35px;background:linear-gradient(90deg,#a00007,#c5000a 50%,#a00007);color:var(--white);font-size:6.4px;padding:13px 0 0 77px}
</style>
</head>
<body>

<header class="site-header abs">
  <a class="brand abs" href="#"><span class="dot"></span>KRVT</a>
  <div class="social abs"><span></span><span></span><span></span><span></span></div>
  <nav class="util-nav abs">Repetoire du personnel<span>-</span>Bloque<span>-</span>Salle de Presse<span>-</span>Nous Joindre<span>-</span>Ffancais</nav>
  <div class="search abs">Search
    <svg width="6" height="6" viewBox="0 0 6 6"><circle cx="2.5" cy="2.5" r="1.8" fill="none" stroke="#777" stroke-width=".8"/><line x1="3.8" y1="3.8" x2="5.6" y2="5.6" stroke="#777" stroke-width=".8"/></svg>
  </div>
  <nav class="main-nav abs">
    <a href="#">A PROPOS DE l'KRVT</a><span class="sep">-</span>
    <a class="active" href="#">PROGRAMMES ET FORMATIONS</a><span class="sep">-</span>
    <a href="#">ETUDIANTS</a><span class="sep">-</span>
    <a href="#">NOUVELLES ET EVENEMENTS</a><span class="sep">-</span>
    <a href="#">ENTERPRISES</a>
  </nav>
</header>

<section class="slider abs" role="img" aria-label="Photo d'étudiants souriants en tenue professionnelle dans une salle de cours">
  <svg class="slide-arrow abs" style="left:22px" width="14" height="14" viewBox="0 0 14 14"><path d="M7 1 1 7l6 6M13 1 7 7l6 6" fill="none" stroke="#fff" stroke-width="2.4"/></svg>
  <svg class="slide-arrow abs" style="left:526px" width="14" height="14" viewBox="0 0 14 14"><path d="M1 1l6 6-6 6M7 1l6 6-6 6" fill="none" stroke="#fff" stroke-width="2.4"/></svg>
  <div class="caption abs">KRVT slogan dummy text lorem Ipsum donor sid comes here&nbsp; »
    <div class="dots abs"><span class="on"></span><span></span><span></span><span></span></div>
  </div>
</section>

<section class="intro abs">
  <h1>KRVT : Devenez LesGestionnaires De</h1>
  <p>Lorem ipsum dolor sit amet, consectetur adipiscing elit. In fermentum dolor non augue pretium egestas. Donec sem eros, tincidunt at congue ut, posuere sit amet est. Vivamus scelerisque viverra odio sit amet laoreet. Ut nec neque non justo rutrum tempor lobortis eu ante. Aliquam sagittis, nibh quis commodo auctor, risus mauris laoreet lectus, id facilisis libero odio nec enim.</p>
  <a class="more" href="#">Learn More</a>
</section>

<main class="panel abs">
  <h2 class="section-title blog-title abs">Blogue</h2>

  <article class="blog-item abs" style="left:15px;top:54px">
    <div class="thumb abs" role="img" aria-label="Portrait d'un homme en costume"><span class="date-tag abs">05 JAN</span></div>
    <div class="blog-text abs"><b>Title Lorem ipsum dolor</b>Ferme ntum dolor non augue elit egestas. eros, tincidunt Lorem ipsum dolor sit amet, Ferme ntum dolor non<div class="meta">By Mensah -<u>Learn More</u></div></div>
  </article>
  <article class="blog-item abs" style="left:226px;top:54px">
    <div class="thumb abs" role="img" aria-label="Portrait d'un homme en costume"><span class="date-tag abs">05 JAN</span></div>
    <div class="blog-text abs"><b>Title Lorem ipsum dolor</b>Ferme ntum dolor non augue elit egestas. eros, tincidunt Lorem ipsum dolor sit amet, Ferme ntum dolor non<div class="meta">By Mensah -<u>Learn More</u></div></div>
  </article>
  <article class="blog-item abs" style="left:15px;top:133px">
    <div class="thumb abs" role="img" aria-label="Portrait d'un homme en costume"><span class="date-tag abs">05 JAN</span></div>
    <div class="blog-text abs"><b>Title Lorem ipsum dolor</b>Ferme ntum dolor non augue elit egestas. eros, tincidunt Lorem ipsum dolor sit amet, Ferme ntum dolor non<div class="meta">By Mensah -<u>Learn More</u></div></div>
  </article>
  <article class="blog-item abs" style="left:226px;top:133px">
    <div class="thumb abs" role="img" aria-label="Portrait d'un homme en costume"><span class="date-tag abs">05 JAN</span></div>
    <div class="blog-text abs"><b>Title Lorem ipsum dolor</b>Ferme ntum dolor non augue elit egestas. eros, tincidunt Lorem ipsum dolor sit amet, Ferme ntum dolor non<div class="meta">By Mensah -<u>Learn More</u></div></div>
  </article>
  <div class="v-div abs"></div>
  <div class="h-div abs"></div>

  <h2 class="section-title events-title abs">Eventments</h2>
  <article class="event-card abs" style="left:15px">
    <svg class="ribbon abs" width="20" height="28" viewBox="0 0 20 28"><path d="M0 0h20v28l-10-6-10 6z" fill="#b30008"/></svg>
    <div class="ribbon abs"><span>05<br><small>JAN</small></span></div>
    <div class="event-text abs"><b>Dummy Event Title Lorem ipsum sit amet,</b>Lorem ipsum dolor sit amet, consecttur adipiscing elit. In fermentum dolor non augue pretium dolor augue pretium egestas egestase. dolor non augue pretium egestas fermentum</div>
    <a class="event-more abs" href="#">Learn More</a>
  </article>
  <article class="event-card abs" style="left:150px">
    <svg class="ribbon abs" width="20" height="28" viewBox="0 0 20 28"><path d="M0 0h20v28l-10-6-10 6z" fill="#b30008"/></svg>
    <div class="ribbon abs"><span>05<br><small>JAN</small></span></div>
    <div class="event-text abs"><b>Dummy Event Title Lorem ipsum sit amet,</b>Lorem ipsum dolor sit amet, consecttur adipiscing elit. In fermentum dolor non augue pretium dolor augue pretium egestas egestase. dolor non augue pretium egestas fermentum</div>
    <a class="event-more abs" href="#">Learn More</a>
  </article>

  <h2 class="section-title tv-title abs">KRVT.tv</h2>
  <div class="video abs" role="img" aria-label="Aperçu vidéo : une étudiante dans une salle de classe">
    <div class="play abs"><svg width="20" height="20" viewBox="0 0 20 20"><path d="M8 5l7 5-7 5z" fill="#111"/></svg></div>
    <div class="controls abs">
      <svg width="119" height="18" viewBox="0 0 119 18">
        <path d="M5 5l6 4-6 4z" fill="#eee"/>
        <path d="M15 7h2l3-3v10l-3-3h-2z" fill="#eee"/>
        <line x1="32" y1="9" x2="58" y2="9" stroke="#aaa" stroke-width="1"/>
        <circle cx="45" cy="9" r="1.6" fill="#fff"/>
        <text x="62" y="11" font-size="5" fill="#ddd" font-family="Open Sans,sans-serif">2:15 - 4:00</text>
        <circle cx="97" cy="9" r="3" fill="none" stroke="#eee" stroke-width="1.6"/>
        <path d="M105 5h3M105 5v3M114 5h-3M114 5v3M105 13h3M105 13v-3M114 13h-3M114 13v-3" stroke="#eee" stroke-width="1"/>
      </svg>
    </div>
  </div>
  <div class="video-label abs">de Videos</div>
</main>

<aside class="side-box news abs">
  <div class="side-tab abs">Text Heading</div>
  <div class="news-item abs" style="top:31px"><div class="news-thumb abs" role="img" aria-label="Photo d'un intervenant"></div><div class="news-text abs"><b>Title Lorem ipsum</b>dolor Ferme ntum dolor non augue elit egestas.»</div></div>
  <div class="news-item abs" style="top:76px"><div class="news-thumb abs" role="img" aria-label="Photo d'un groupe d'étudiants"></div><div class="news-text abs"><b>Title Lorem ipsum</b>dolor Ferme ntum dolor non augue elit egestas.»</div></div>
  <div class="news-item abs" style="top:121px"><div class="news-thumb abs" role="img" aria-label="Photo d'une réunion"></div><div class="news-text abs"><b>Title Lorem ipsum</b>dolor Ferme ntum dolor non augue elit egestas.»</div></div>
  <a class="view-all abs" href="#">View All</a>
</aside>

<aside class="side-box audience abs" role="img" aria-label="Photo d'un homme en costume souriant en arrière-plan">
  <div class="side-tab abs">Vous Etes</div>
  <ul>
    <li>Futur Etudiant</li><li>Etudiant Actuel</li><li>Entreprise</li><li>Employeur</li><li>Postulant</li><li>Medias</li><li>Partenaires</li>
  </ul>
  <a class="more-links abs" href="#">More Links</a>
</aside>

<section class="partners abs" aria-label="Partenaires">
  <span></span><span></span><span></span><span></span><span></span><span></span><span></span>
</section>

<footer class="site-footer abs">
  <div class="foot-col abs" style="left:98px">
    <h3><svg width="14" height="9" viewBox="0 0 14 9"><path d="M0 2h8l2-2h4v2h-3v2h2v2h-2v2h-1H3L0 6z" fill="#fff"/></svg>A Propos</h3>
    <ul><li>A Propos</li><li>A Propos de l'KRVT</li><li>Admissions</li><li>Calendrier De l'ecole</li><li>Offres d'emloi</li><li>Repertoir du personnel</li></ul>
  </div>
  <div class="foot-col abs" style="left:212px">
    <h3><svg width="14" height="9" viewBox="0 0 14 9"><path d="M0 2h8l2-2h4v2h-3v2h2v2h-2v2h-1H3L0 6z" fill="#fff"/></svg>Etudiants</h3>
    <ul><li>A Propos</li><li>A Propos de l'KRVT</li><li>Admissions</li><li>Calendrier De l'ecole</li><li>Offres d'emloi</li><li>Repertoir du personnel</li></ul>
  </div>
  <div class="foot-col abs" style="left:322px">
    <h3><svg width="14" height="9" viewBox="0 0 14 9"><path d="M0 2h8l2-2h4v2h-3v2h2v2h-2v2h-1H3L0 6z" fill="#fff"/></svg>KRVT</h3>
    <p>12, Rue des Palmiers<br>Quartier Nord, Pres du Marche<br>Central</p>
    <div class="phone">
      <svg width="7" height="18" viewBox="0 0 7 18"><path d="M5 1C1 3 1 15 5 17l1.5-3L5 12c-1-2-1-4 0-6l1.5-2z" fill="#ddd"/></svg>
      <span>[000] 55 010 20 30<br>[000] 55 010 40 50</span>
    </div>
    <div class="foot-social"><span></span><span></span><span></span><span></span></div>
  </div>
  <div class="foot-col abs" style="left:448px">
    <h3><svg width="11" height="8" viewBox="0 0 11 8"><rect width="11" height="8" fill="#fff"/><path d="M0 0l5.5 4.5L11 0" fill="none" stroke="#2b2724" stroke-width="1"/></svg>Infolettre</h3>
    <p style="width:118px;line-height:8px">Lorem ipsum dolor Ferme ntum sid dolor non augue elit egestas. eros, tincidunt Lorem ipsum dolor sit amet, Ferme ntum dolor non</p>
    <div class="email">Enter Email</div>
    <span class="subscribe">Subscribe Me</span>
  </div>
  <div class="foot-brand abs"><span class="dot"></span>KRVT</div>
</footer>

<div class="copyright abs">Copyright KRVT 2014&nbsp; [ Privacy Policy ]&nbsp; [ Cookies ]&nbsp; [ Legal Information ]</div>

</body>
</html>
```